Web Design Project for Velorasa cloud based service

None of us is a designer, and ENGLISH is not our first language, but we need to make sure that those bidding for this project understand that we're just looking for the creative components in order to build a website and we don't need you to create all the pages and /or diagram the website for us. Please ask as many questions as you want for us to ensure we don't waste your time.

Content and Community Management System
- We need a redesign of the Back Office Screens
o The kind of screen detailed on the (file 2 attached bellow) “Velorasa Some Screens.pptx”
- Following, as a strong reference te velorasa logo design line (file 1 attached bellow)
- We DO NOT need application, or implementation, only the following SOW.

Scope of Work (SOW) by components that we need:
- Main Theme
- Tables
- Buttons
- Icons
- Lists
- Form elements

OUT of Scope (we DO NOT need it):
· Emerging Windows implementation (jquery – lightbox)
· Layout (we do not need you to create the layout for us)
· Module Development (Css 3, jQuery, Html 5)

Reason: We're extending the deadline in order to have more options to select. The current option do not fit our expectation yet. Any question, please do it. Many thanks. Velorasa Team.

Hi designers!

We've [a] extended the deadline in order to have more choices and we made a change on the Power Point file attached with [b] the 3 most important screen than include all the components/element we need designed from you.

We wait for your proposal.
Let's do it!

Many Thanks.
Best regards.

velorasa Team.

```html
<!DOCTYPE html>
<html lang="en">
<head>
<meta charset="utf-8">
<title>Velorasa – Back Office UI Kit</title>
<link href="https://fonts.googleapis.com/css2?family=Arimo:wght@400;700&display=swap" rel="stylesheet">
<style>
:root{
  --orange:#ff6a13;
  --orange-dark:#e85a05;
  --ink:#222;
  --dark:#232323;
  --text:#555;
  --muted:#888;
  --line:#ddd;
  --error:#c9302c;
  --focus:#7fb6e8;
  --stripe:#f7f7f7;
}
*{box-sizing:border-box;margin:0;padding:0}
html,body{width:1200px;height:1067px;overflow:hidden}
body{position:relative;background:#fff;font-family:"Arimo",Arial,sans-serif;color:var(--text);font-size:12px}
.abs{position:absolute}

/* top bar */
.topbar{left:0;top:0;width:1200px;height:38px;background:var(--dark);border-bottom:1px solid #000}
.user-status{right:357px;top:13px;color:#fff;font-size:12px}
.user-status b{color:var(--orange)}
.pill{top:5px;height:28px;border-radius:14px;background:linear-gradient(#f4f4f4,#cfcfcf);color:#555;font-size:12px;line-height:28px;text-align:center}

/* header */
.header-rule{left:0;top:236px;width:1200px;border-top:1px solid #ccc;z-index:1}
.brand{left:127px;top:150px;display:flex;align-items:center;gap:10px}
.brand-mark{width:22px;height:22px;background:var(--orange)}
.brand-name{font-size:25px;font-weight:700;color:var(--ink);letter-spacing:-0.5px}

.nav-btn{top:115px;height:40px;border-radius:4px;font-size:12px;font-weight:700;line-height:40px;text-align:center;background:linear-gradient(#fff,#f1f1f1);border:1px solid #e3e3e3;box-shadow:0 2px 3px rgba(0,0,0,.12);color:#999}
.nav-btn.active{background:var(--orange);border-color:var(--orange);color:#fff;box-shadow:none}
.nav-btn.active::after{content:"";position:absolute;left:48px;bottom:-8px;border:8px solid transparent;border-bottom:0;border-top-color:var(--orange)}
.nav-btn.open{height:56px;border-bottom:none;border-radius:4px 4px 0 0;box-shadow:0 -1px 3px rgba(0,0,0,.08);color:var(--orange);line-height:40px;background:#fff;z-index:4}
.nav-btn.hover{color:var(--orange)}
.nav-btn svg{vertical-align:-3px;margin-right:6px}
.subnav{left:516px;top:170px;width:192px;height:126px;background:#f4f4f4;border:1px solid #e3e3e3;border-radius:0 0 4px 4px;box-shadow:0 3px 4px rgba(0,0,0,.2);padding:0 16px;z-index:3}
.subnav li{list-style:none;height:41px;line-height:42px;color:#999;font-weight:700;border-bottom:1px dotted #bbb;font-size:12px;white-space:nowrap}
.subnav li:last-child{border:none}
.subnav svg{vertical-align:-1px;margin-right:5px}
.cursor{left:753px;top:138px;z-index:5}

/* content */
.h-section{left:119px;top:289px;font-size:24px;font-weight:700;color:var(--orange)}
.h-sub{left:119px;top:329px;font-size:18px;font-weight:700;color:var(--ink)}
.body-copy{left:119px;top:354px;width:620px;font-size:12px;line-height:21px;color:var(--text)}

.data-table{left:119px;top:450px;width:623px;border-collapse:collapse;font-size:13px;color:#444}
.data-table th{height:35px;text-align:left;font-weight:700;color:#333;padding-left:9px}
.data-table td{height:35px;border-top:1px solid var(--line);padding-left:9px}
.data-table tbody tr:nth-child(odd){background:var(--stripe)}
.c1{width:65px}.c2{width:234px}.c3{width:230px}

.field-label{width:140px;text-align:right;font-size:13px;color:#333}
.field{left:278px;width:280px;height:28px;border:1px solid #ddd;border-radius:3px;padding-left:6px;font-size:13px;line-height:26px;color:#555}
.field.focused{border-color:var(--focus);box-shadow:0 0 4px rgba(82,168,236,.5)}
.field.locked{background:#fff;color:#666}
.field.invalid{width:220px;border-color:var(--error)}
.is-error{color:var(--error)}

.form-actions{left:118px;top:800px;width:624px;height:63px;background:#f3f3f3;border-top:1px solid #ddd}
.btn{top:818px;height:28px;border-radius:3px;font-size:13px;line-height:28px;text-align:center}
.btn-primary{left:278px;width:103px;background:linear-gradient(var(--orange),var(--orange-dark));color:#fff}
.btn-default{left:386px;width:60px;background:linear-gradient(#fff,#e6e6e6);border:1px solid #ccc;color:#333}

/* sidebar */
.sidebar{left:761px;top:283px;width:320px;height:288px;background:var(--dark);border-radius:7px;padding:24px 28px 0 28px}
.sidebar h3{font-size:18px;font-weight:400;color:#fff;letter-spacing:.3px;margin-bottom:3px}
.sidebar li{list-style:none;height:38px;line-height:38px;border-bottom:1px dotted #444;color:#fff;font-weight:700;font-size:12px;display:flex;align-items:center}
.sidebar li:last-child{border:none}
.plus{width:15px;height:15px;border-radius:50%;background:var(--orange);margin-right:6px;position:relative;flex:none}
.plus::before,.plus::after{content:"";position:absolute;background:#fff;left:3.5px;top:6.5px;width:8px;height:2px}
.plus::after{left:6.5px;top:3.5px;width:2px;height:8px}

/* footer */
.footer-band{left:0;top:902px;width:1200px;height:165px;background:var(--dark)}
.footer-col{top:935px;font-size:12px;line-height:21px}
.footer-col h4{color:#fff;font-weight:700;font-size:12px}
.footer-col a{display:block;color:var(--orange);text-decoration:none}
.copyright{right:218px;top:984px;text-align:right;color:#fff;font-size:12px;line-height:21px}
.footer-brand{left:997px;top:1003px;font-size:16px;font-weight:700;color:var(--orange)}
</style>
</head>
<body>

<header>
  <div class="abs topbar"></div>
  <div class="abs user-status">Loged in as <b>UserName</b></div>
  <div class="abs pill" style="left:856px;width:137px">Change Password</div>
  <div class="abs pill" style="left:1001px;width:76px">Log out</div>

  <div class="abs brand"><span class="brand-mark"></span><span class="brand-name">VELORASA</span></div>

  <div class="abs header-rule"></div>

  <nav>
    <div class="abs nav-btn active" style="left:390px;width:110px">BTN ACTIVE</div>
    <div class="abs nav-btn open" style="left:516px;width:124px">WITH SUB-NAV</div>
    <div class="abs nav-btn hover" style="left:656px;width:110px">ROLLOVER</div>
    <div class="abs nav-btn" style="left:781px;width:110px">BUTTON #1</div>
    <div class="abs nav-btn" style="left:906px;width:175px"><svg width="18" height="15" viewBox="0 0 18 15"><path d="M9 0L0 8h2.5v7h5v-5h3v5h5V8H18L14.5 5V1h-2v2.2z" fill="#999"/></svg>BUTTON WITH ICON</div>
    <ul class="abs subnav">
      <li><svg width="11" height="11" viewBox="0 0 11 11"><path d="M3 2.3A4.3 4.3 0 1 0 8 2.3" fill="none" stroke="#999" stroke-width="1.6"/><path d="M5.5 0v5" stroke="#999" stroke-width="1.6"/></svg>SubNavigation link #1</li>
      <li><svg width="12" height="9" viewBox="0 0 12 9"><rect x="0" y="7" width="2" height="2" fill="#999"/><rect x="3" y="5" width="2" height="4" fill="#999"/><rect x="6" y="3" width="2" height="6" fill="#999"/><rect x="9" y="0" width="2" height="9" fill="#999"/></svg>SubNavigation link #2</li>
      <li><svg width="11" height="11" viewBox="0 0 11 11"><circle cx="5.5" cy="5.5" r="3.4" fill="none" stroke="#999" stroke-width="2.4" stroke-dasharray="2 1.2"/><circle cx="5.5" cy="5.5" r="2.4" fill="#999"/><circle cx="5.5" cy="5.5" r="1" fill="#f4f4f4"/></svg>SubNavigation link #3</li>
    </ul>
    <svg class="abs cursor" width="26" height="34" viewBox="0 0 26 34"><path d="M2 2v26l7-7 5 11 4-2-5-10h10z" fill="#2a2220" stroke="#fff" stroke-width="1.5"/></svg>
  </nav>
</header>

<main>
  <h1 class="abs h-section">Headings &amp; body copy</h1>
  <h2 class="abs h-sub">Typographic scale</h2>
  <p class="abs body-copy">Sed egestas, ante et vulputate volutpat, eros pede semper est, vitae luctus metus libero eu augue. Morbi purus libero, faucibus adipiscing, commodo quis, gravida id, est. Sed lectus. Praesent elementum hendrerit tortor. Sed semper lorem at felis. Vestibulum volutpat, lacus a ultrices sagittis, mi neque euismod dui, eu pulvinar nunc sapien ornare nisl. Phasellus pede arcu, dapibus eu, fermentum et, dapibus sed, urna.</p>

  <table class="abs data-table">
    <thead><tr><th class="c1">#</th><th class="c2">First Name</th><th class="c3">Last Name</th><th>Username</th></tr></thead>
    <tbody>
      <tr><td>1</td><td>Mara</td><td>Olsen</td><td>@mol</td></tr>
      <tr><td>2</td><td>Jonas</td><td>Thorne</td><td>@jth</td></tr>
      <tr><td>3</td><td>Leo</td><td>the Finch</td><td>@chirper</td></tr>
    </tbody>
  </table>

  <form>
    <label class="abs field-label" style="left:118px;top:642px">Focused input</label>
    <div class="abs field focused" style="top:635px">This is focused...</div>
    <label class="abs field-label" style="left:118px;top:688px">Uneditable input</label>
    <div class="abs field locked" style="top:681px">Some value here</div>
    <label class="abs field-label is-error" style="left:118px;top:741px">Input with error</label>
    <div class="abs field invalid" style="top:735px"></div>
    <span class="abs is-error" style="left:507px;top:741px;font-size:13px">Please correct the error</span>
    <div class="abs form-actions"></div>
    <div class="abs btn btn-primary">Save changes</div>
    <div class="abs btn btn-default">Cancel</div>
  </form>

  <aside class="abs sidebar">
    <h3>SIDEBAR CONTENT</h3>
    <ul>
      <li><span class="plus"></span>Sed egestas ante et vulputate volutpat</li>
      <li><span class="plus"></span>Eros pede semper est, vitae luctus metus</li>
      <li><span class="plus"></span>Libero eu augue. Morbi purus libero</li>
      <li><span class="plus"></span>Faucibus adipiscing</li>
      <li><span class="plus"></span>Commodo quis gravida id est.</li>
      <li><span class="plus"></span>Sed lectus</li>
    </ul>
  </aside>
</main>

<footer>
  <div class="abs footer-band" role="img" aria-label="Dark footer band with a decorative scalloped top edge"></div>
  <div class="abs footer-col" style="left:120px"><h4>Text of the link #1</h4><a href="#">sublink a</a><a href="#">sublink b</a><a href="#">sublink c</a></div>
  <div class="abs footer-col" style="left:277px"><h4>Text of the link #2</h4><a href="#">sublink a</a><a href="#">sublink b</a></div>
  <div class="abs footer-col" style="left:433px"><h4>Text of the link #3</h4><a href="#">sublink a</a><a href="#">sublink b</a><a href="#">sublink c</a><a href="#">sublink d</a></div>
  <div class="abs footer-col" style="left:590px"><h4>Text of the link #4</h4><a href="#">sublink a</a><a href="#">sublink b</a><a href="#">sublink c</a></div>
  <div class="abs copyright">© copyright 2012.<br>All Rights Reserved</div>
  <div class="abs footer-brand">VELORASA</div>
</footer>

</body>
</html>
```